KTV Lanternfall

I need a graphic package design for our new bodybuilding sports supplement. The artwork should be clean and useable for many formats. examples or great usage are www.ferrovigorlab.example, www.quartzpulse.example and http://www.belwinnutrition.example/ as examples. I am adding our logo for your reference. The name Lanternfall is because it will help make "Big Guns" as a catch phrase, the product line will have other supplements such as creatine and protein powders and the artwork should be useable on all products. You can see our website for ideas at www.kestovalife.example
Updates

Hi everyone, There are some nice entries coming in. I do wonder if some of you are reading the brief as a few labels don't even highlight the product, KTV is the company, Lanternfall is the Product. Thanks Tam

Industry/Entity Type

Supplement

```html
<!DOCTYPE html>
<html lang="en">
<head>
<meta charset="utf-8">
<title>KTV Lanternfall Series – Isolate Label</title>
<link rel="stylesheet" href="https://fonts.googleapis.com/css2?family=Audiowide&family=Russo+One&family=Saira:wght@400;600&display=swap">
<style>
  :root {
    --stage-light: #4a4a4a;
    --stage-dark: #0d0d0d;
    --label-deep: #1f4a0e;
    --label-mid: #4f8f1c;
    --label-bright: #c9f06a;
    --glow: #f6ffd8;
    --logo-ink: #1a1a1a;
    --headline-fill: #e4f7a0;
    --headline-edge: #2d3a10;
    --claim-fill: #c9d98a;
    --claim-edge: #28360d;
  }
  * { margin: 0; padding: 0; box-sizing: border-box; }
  html, body {
    width: 1200px; height: 1128px; overflow: hidden;
  }
  body {
    background: radial-gradient(ellipse at 50% 45%, var(--stage-light) 0%, #262626 55%, var(--stage-dark) 100%);
    position: relative;
  }
  .label {
    position: absolute;
    left: 150px; top: 280px;
    width: 900px; height: 570px;
    overflow: hidden;
    background:
      radial-gradient(circle at 46% 30%, var(--glow) 0%, rgba(230,255,170,0.7) 10%, rgba(160,215,80,0) 38%),
      radial-gradient(ellipse at 80% 90%, rgba(210,240,110,0.55) 0%, rgba(210,240,110,0) 45%),
      linear-gradient(180deg, var(--label-mid) 0%, #6aa824 45%, var(--label-deep) 100%);
  }
  .label__light {
    position: absolute; inset: 0;
  }
  .brand-row {
    position: absolute; left: 110px; top: 55px;
    display: flex; align-items: flex-start; gap: 50px;
  }
  .company-name {
    font-family: "Saira", sans-serif;
    font-weight: 600;
    font-size: 70px;
    color: var(--logo-ink);
    line-height: 1;
    letter-spacing: 2px;
    margin-top: 12px;
  }
  .product-line { text-align: right; }
  .product-name {
    font-family: "Russo One", sans-serif;
    font-size: 76px;
    line-height: 1;
    color: var(--headline-fill);
    -webkit-text-stroke: 2px var(--headline-edge);
    text-shadow: 3px 4px 3px rgba(0,0,0,0.45);
    letter-spacing: 1px;
  }
  .series-tag {
    font-family: "Russo One", sans-serif;
    font-size: 22px;
    color: #b9c884;
    -webkit-text-stroke: 0.8px var(--headline-edge);
    margin-top: 2px;
    letter-spacing: 1px;
  }
  .variant {
    position: absolute; left: 0; right: 0; top: 195px;
    text-align: center;
    font-family: "Audiowide", sans-serif;
    font-size: 124px;
    line-height: 1;
    color: var(--headline-fill);
    -webkit-text-stroke: 3px var(--headline-edge);
    text-shadow: 4px 6px 4px rgba(0,0,0,0.45);
    letter-spacing: 4px;
  }
  .claims {
    position: absolute; top: 365px; left: 0; right: 0;
    list-style: none;
    font-family: "Russo One", sans-serif;
    font-size: 26px;
    line-height: 42px;
    color: var(--claim-fill);
    -webkit-text-stroke: 0.8px var(--claim-edge);
    text-shadow: 2px 2px 2px rgba(0,0,0,0.4);
  }
  .claims li { position: relative; padding-left: 24px; }
  .claims li::before {
    content: ""; position: absolute; left: 0; top: 14px;
    border-left: 12px solid #e8f2b8;
    border-top: 7px solid transparent;
    border-bottom: 7px solid transparent;
  }
  .claims li:nth-child(1) { margin-left: 45px; }
  .claims li:nth-child(2) { margin-left: 145px; }
  .claims li:nth-child(3) { margin-left: 235px; }
  .claims li:nth-child(4) { margin-left: 330px; }
</style>
</head>
<body>
  <section class="label">
    <div class="label__light" role="img" aria-label="Soft green bokeh light glow behind the label text"></div>

    <div class="brand-row">
      <div class="company-name">KTV</div>
      <div class="product-line">
        <div class="product-name">LANTERNFALL</div>
        <div class="series-tag">SERIES</div>
      </div>
    </div>

    <h1 class="variant">ISOLATE</h1>

    <ul class="claims">
      <li>HELPS BUILD LEAN MUSCLE AND STRENGTH</li>
      <li>SUPPORTS RECOVERY AFTER EXCERSIZE</li>
      <li>INSTANTIZED FOR EASY MIXING</li>
      <li>LOW IN FAT</li>
    </ul>
  </section>
</body>
</html>
```